Brightmoor Partners Branding Revamp

We are a consulting company, looking for a way to display and promote our brand. We have 2 sides to the business- Brightmoor (financial) and Partners (cyber security). The financial side products relate to business necessities: card processing, website design/hosting/maintenance, VoIP phone systems. The cyber security side promotes a bundled package of 4 solutions: network vulnerability scan, dark web scan, anti-ransomeware/malware software, and image-level backups. We want people to understand that partnering with Brightmoor Partners gives them “Elevated Peace of Mind” (tagline). Current badge and logos uploaded.

Target Market(s)

Small businesses

Contact Information for Business Card

Lena Marwick, Vice President, lena@brightmoorpartners.example, 555-806-1937, www.brightmoorpartners.example

Requirements
Nice to have
• I do prefer the darker background for front and back

```html
<!DOCTYPE html>
<html lang="en">
<head>
<meta charset="UTF-8">
<title>Brightmoor Partners – Business Card</title>
<link rel="stylesheet" href="https://fonts.googleapis.com/css2?family=Open+Sans:wght@400;600&display=swap">
<style>
  :root {
    --stage: #3a3a3a;
    --stage-dark: #1e1e1e;
    --card: #141414;
    --card-edge: #e0141c;
    --red: #e3161e;
    --red-deep: #a50d12;
    --white: #f4f4f4;
    --grey: #c9c9c9;
  }
  * { margin: 0; padding: 0; box-sizing: border-box; }
  html, body { width: 1200px; height: 900px; overflow: hidden; }
  body {
    background: radial-gradient(ellipse at 55% 50%, var(--stage) 0%, var(--stage-dark) 85%);
    font-family: "Open Sans", Arial, sans-serif;
    position: relative;
  }
  .card {
    position: absolute;
    left: 300px;
    width: 600px;
    height: 343px;
    background: var(--card);
    border-radius: 22px;
    box-shadow: 0 0 0 3px var(--card-edge), 0 18px 40px rgba(0,0,0,.55);
    overflow: hidden;
  }
  .card--front { top: 68px; }
  .card--back { top: 489px; }

  /* wordmark */
  .wordmark { display: flex; align-items: center; gap: 18px; }
  .wordmark__square { width: 34px; height: 34px; background: var(--red); }
  .wordmark__text { color: var(--white); font-weight: 600; line-height: 1; text-transform: uppercase; }
  .wordmark__main { display: block; letter-spacing: .38em; }
  .wordmark__sub { display: block; letter-spacing: .32em; }

  .card--front .wordmark {
    position: absolute; left: 50%; top: 50%;
    transform: translate(-50%, -50%);
  }
  .card--front .wordmark__main { font-size: 34px; }
  .card--front .wordmark__sub { font-size: 14px; margin-top: 12px; }

  .card--back .wordmark { position: absolute; left: 44px; top: 34px; }
  .card--back .wordmark__square { width: 18px; height: 18px; }
  .card--back .wordmark__main { font-size: 20px; }
  .card--back .wordmark__sub { font-size: 8px; margin-top: 6px; }

  .brand-mark {
    position: absolute; left: 412px; top: 120px;
    width: 150px; height: 150px;
    background: linear-gradient(135deg, var(--red) 0%, var(--red-deep) 100%);
  }

  .person { position: absolute; left: 44px; top: 100px; }
  .person__bar { position: absolute; left: 0; top: 4px; width: 8px; height: 26px; background: var(--red); }
  .person__name {
    margin-left: 34px; color: var(--red);
    font-size: 30px; font-weight: 400; text-transform: uppercase; letter-spacing: -.01em; line-height: 1.1;
  }
  .person__title { margin-left: 34px; color: var(--grey); font-size: 15px; text-transform: uppercase; margin-top: 2px; }
  .person__rule { margin: 12px 0 0 34px; width: 16px; height: 2px; background: var(--red); }

  .contact { position: absolute; left: 78px; top: 212px; list-style: none; }
  .contact__item {
    display: flex; align-items: center; gap: 9px;
    color: var(--white); font-size: 16px; line-height: 1.6;
  }
  .contact__icon { width: 11px; height: 11px; flex: none; }
</style>
</head>
<body>

<section class="card card--front" aria-label="Card front">
  <div class="wordmark">
    <span class="wordmark__square"></span>
    <span class="wordmark__text">
      <span class="wordmark__main">Brightmoor</span>
      <span class="wordmark__sub">Partners</span>
    </span>
  </div>
</section>

<section class="card card--back" aria-label="Card back">
  <div class="wordmark">
    <span class="wordmark__square"></span>
    <span class="wordmark__text">
      <span class="wordmark__main">Brightmoor</span>
      <span class="wordmark__sub">Partners</span>
    </span>
  </div>

  <div class="brand-mark" role="img" aria-label="Large brand emblem area"></div>

  <div class="person">
    <span class="person__bar"></span>
    <h1 class="person__name">Lena Marwick</h1>
    <p class="person__title">Vice President</p>
    <div class="person__rule"></div>
  </div>

  <ul class="contact">
    <li class="contact__item">
      <svg class="contact__icon" viewBox="0 0 12 12"><path d="M2.5 1 L4.5 1 L5.3 3.6 L4 4.6 Q5 7 7.4 8 L8.4 6.7 L11 7.5 L11 9.5 Q10 11 8.5 11 Q1 10 1 3.5 Q1 2 2.5 1Z" fill="#e3161e"/></svg>
      +1 555-806-1937
    </li>
    <li class="contact__item">
      <svg class="contact__icon" viewBox="0 0 12 12"><rect x="1" y="2.5" width="10" height="7" rx="1" fill="none" stroke="#e3161e" stroke-width="1.4"/><path d="M1.5 3 L6 6.5 L10.5 3" fill="none" stroke="#e3161e" stroke-width="1.2"/></svg>
      lena@brightmoorpartners.example
    </li>
    <li class="contact__item">
      <svg class="contact__icon" viewBox="0 0 12 12"><circle cx="6" cy="6" r="4.8" fill="none" stroke="#e3161e" stroke-width="1.3"/><ellipse cx="6" cy="6" rx="2" ry="4.8" fill="none" stroke="#e3161e" stroke-width="1"/><path d="M1.2 6 H10.8" stroke="#e3161e" stroke-width="1"/></svg>
      www.brightmoorpartners.example
    </li>
  </ul>
</section>

</body>
</html>
```